Create a professional, fresh and polished oversized post card for law firm specializing in Estate Planning & Probate Law for High Net Worth Clients

Use any picture(s) of your choice (mine or ones you recommend), logo, headshot and company info

www.morvenashcroftlaw.com

Westgate Office - 4100 Birchmont Road, Suite 1500, Charlotte, NC 28214
Kerrington Office - 13480 Oakridge Lane, Suite 300, Charlotte, NC 28269

Phone (704) 555-0187

Use this card for a Free Consultation

Target Market(s)

young and old families too; business owners

Industry/Entity Type

Law Firm

Font styles to use
Serif
Sans Serif

Requirements
Must have
• Use any picture(s) of your choice (mine or ones you recommend), logo, headshot and company info
• www.morvenashcroftlaw.com
• Westgate Office - 4100 Birchmont Road, Suite 1500, Charlotte, NC 28214
• Kerrington Office - 13480 Oakridge Lane, Suite 300, Charlotte, NC 28269
• Phone (704) 555-0187
• Use this card for a Free Consultation
Nice to have
• great colors and great design; like graphics with depth /shading
Should not have
• don't use too many pics - keep it simple

```html
<!DOCTYPE html>
<html lang="en">
<head>
<meta charset="utf-8">
<title>Morven Ashcroft Law, PLLC – Postcard</title>
<link rel="stylesheet" href="https://fonts.googleapis.com/css2?family=Bitter:wght@400;500;600&family=Open+Sans:wght@300;400&display=swap">
<style>
  :root{
    --teal:#127ba3;
    --teal-mid:#0e6a8e;
    --teal-dark:#0b4a68;
    --navy:#0a3d5c;
    --band-light:#0a84ad;
    --grey-band:#d9dadc;
    --grey-text:#747578;
    --grey-light:#8f9194;
    --ring:#8d8f92;
    --ink:#1d1d1f;
    --white:#ffffff;
  }
  html,body{margin:0;padding:0;overflow:hidden;background:var(--white);}
  .postcard{position:relative;width:1200px;height:770px;overflow:hidden;background:var(--white);font-family:"Bitter",Georgia,serif;}
  .postcard svg.shapes{position:absolute;left:0;top:0;}
  .t{position:absolute;margin:0;white-space:nowrap;line-height:1;}
  .center{transform:translateX(-50%);text-align:center;}

  .firm-name{left:825px;top:45px;font-size:24px;font-weight:600;color:var(--teal);}
  .firm-email{left:825px;top:79px;font-family:"Open Sans",Arial,sans-serif;font-weight:300;font-size:17px;color:var(--grey-light);}
  .firm-web{left:825px;top:102px;font-size:19px;color:var(--grey-text);}

  .attorney-name{left:515px;top:147px;font-size:29px;font-weight:500;color:var(--teal);}
  .attorney-credentials{left:515px;top:183px;font-size:16px;color:var(--grey-light);}
  .attorney-cert{left:515px;top:218px;font-size:16px;line-height:20px;color:var(--ink);}

  .cta-label{left:470px;top:314px;font-size:20px;font-weight:600;color:var(--teal);}
  .cta-phone{left:320px;top:343px;color:var(--grey-text);}
  .cta-phone .call{font-family:"Open Sans",Arial,sans-serif;font-size:20px;}
  .cta-phone .number{font-family:"Open Sans",Arial,sans-serif;font-size:42px;font-weight:300;letter-spacing:1px;}

  .brand-name{left:206px;top:556px;font-size:36px;font-weight:500;color:var(--teal);}
  .brand-suffix{left:202px;top:607px;font-size:19px;font-weight:500;color:var(--teal);letter-spacing:1px;}

  .office-title{font-size:24px;color:var(--teal);left:473px;}
  .office-address{font-size:18px;line-height:22px;color:var(--grey-text);left:473px;}
  .westgate-title{top:451px;}
  .westgate-address{top:486px;}
  .kerrington-title{top:570px;}
  .kerrington-address{top:605px;}

  .tagline{left:22px;top:669px;font-size:20px;line-height:24px;color:var(--white);}
  .associate{left:22px;top:733px;font-size:20px;color:var(--white);}
</style>
</head>
<body>
<main class="postcard">
  <svg class="shapes" width="1200" height="770" viewBox="0 0 1200 770">
    <defs>
      <radialGradient id="headshotFill" cx="50%" cy="45%" r="60%">
        <stop offset="0%" stop-color="#d9b98e"/>
        <stop offset="55%" stop-color="#9a7a55"/>
        <stop offset="100%" stop-color="#1c1a1a"/>
      </radialGradient>
    </defs>
    <!-- contact rules -->
    <line x1="659" y1="36" x2="991" y2="36" stroke="var(--teal)" stroke-width="1.6" stroke-dasharray="1.6 2.6"/>
    <line x1="659" y1="131" x2="991" y2="131" stroke="var(--teal)" stroke-width="1.6" stroke-dasharray="1.6 2.6"/>
    <line x1="376" y1="208" x2="654" y2="208" stroke="var(--teal)" stroke-width="1.6" stroke-dasharray="1.6 2.6"/>

    <!-- appointment band -->
    <polygon class="grey-band" points="0,302 707,302 614,394 0,394" fill="var(--grey-band)"/>
    <polygon points="320,271 400,271 426,297 320,297" fill="var(--band-light)"/>
    <polygon points="400,271 530,271 556,297 426,297" fill="var(--teal-mid)"/>
    <polygon points="530,271 682,271 707,297 556,297" fill="var(--teal-dark)"/>

    <!-- headshot -->
    <circle cx="194" cy="197" r="156" fill="var(--white)" stroke="var(--ring)" stroke-width="5"/>
    <circle cx="194" cy="197" r="149" fill="url(#headshotFill)" role="img" aria-label="Portrait photo of attorney Morven L. Ashcroft"/>

    <!-- brand block -->
    <circle cx="202" cy="472" r="52" fill="var(--teal-dark)" stroke="var(--ink)" stroke-width="2"/>
    <line x1="46" y1="535" x2="356" y2="535" stroke="var(--ink)" stroke-width="2"/>
    <line x1="46" y1="617" x2="146" y2="617" stroke="var(--ink)" stroke-width="2"/>
    <line x1="258" y1="617" x2="356" y2="617" stroke="var(--ink)" stroke-width="2"/>

    <!-- office rules -->
    <line x1="473" y1="480" x2="659" y2="480" stroke="var(--teal)" stroke-width="1.6" stroke-dasharray="1.6 2.6"/>
    <line x1="473" y1="599" x2="661" y2="599" stroke="var(--teal)" stroke-width="1.6" stroke-dasharray="1.6 2.6"/>
    <line x1="768" y1="348" x2="768" y2="664" stroke="var(--ink)" stroke-width="2"/>

    <!-- footer bands -->
    <polygon points="0,658 270,658 330,719 0,719" fill="var(--teal-mid)"/>
    <polygon points="0,719 365,719 416,770 0,770" fill="var(--navy)"/>
  </svg>

  <h1 class="t center firm-name">Morven Ashcroft Law, PLLC</h1>
  <p class="t center firm-email">morven@morvenashcroftlaw.com</p>
  <p class="t center firm-web">www.morvenashcroftlaw.com</p>

  <h2 class="t center attorney-name">Morven L. Ashcroft</h2>
  <p class="t center attorney-credentials">Attorney, CPA, CFM, CMA, MAc.</p>
  <p class="t center attorney-cert">Board Certified Specialist in<br>Estate Planning and Probate Law</p>

  <p class="t center cta-label">To schedule an appointment</p>
  <p class="t cta-phone"><span class="call">call </span><span class="number">704-555-0187</span></p>

  <p class="t center brand-name">Morven Ashcroft</p>
  <p class="t center brand-suffix">LAW PLLC</p>

  <h3 class="t office-title westgate-title">Westgate Office</h3>
  <p class="t office-address westgate-address">4100 Birchmont Road, Suite 1500<br>Charlotte, NC 28214</p>
  <h3 class="t office-title kerrington-title">Kerrington Office</h3>
  <p class="t office-address kerrington-address">13480 Oakridge Lane, Suite 300<br>Charlotte, NC 28269</p>

  <p class="t tagline">Charlotte Estate Planning<br>&amp; Probate Attorneys</p>
  <p class="t associate">Nora Whitfield Delaney Attorney</p>
</main>
</body>
</html>
```